IT company developing solutions for air cargo industry is looking for a new website

We are a professional IT company developing solutions for air cargo industry worldwide.

We are looking to update and completely redesign our current webpages: https://www.brimleaftech.cz/

What we like about our current pages are the animated graphics on the home page. These could stay, but not a must.

The design of the new pages should be very modern, clean, unique, creative, professional, and to make a statement. We are looking for animated graphics, cool and interesting interactions, cascading layers, etc.

Our company logo is yellow, gray and black. You don’t necessarily have to stick to this colour scheme, however the corporate colors should work well with the overal design of the web pages.
Dark mode pages are also an option.

The scope of the project would include creating a:

• Header
• Footer
• Landing page
• Navigation bar (8 tabs)
• Subpages (10)

In the first stage we are looking only for the header / footer / landing page with navigaton bar / Solutions page design.
As a second round, finalists might be asked to submit another section of the website to see their consistency in terms of the look and feel proposed for the Homepage and Solutions’ pages.
The winning designer will then complete the rest of the pages.

Attached you will find a brief for the first scope of the project. Please read the note section on slide nr. 3 carefully to understand, what we exactly are looking for to achieve.

Industry/Entity Type

Aviation

Number of Pages Required

1 page

Requirements
Must have
• See brief
Nice to have
• See brief
Should not have
• See brief

```html
<!DOCTYPE html>
<html lang="en">
<head>
<meta charset="utf-8">
<title>Brimleaf Tech — Air Cargo IT Solutions</title>
<link href="https://fonts.googleapis.com/css2?family=Exo+2:wght@500;600&family=Nunito:wght@300;400;600;700;800&display=swap" rel="stylesheet">
<style>
  :root {
    --yellow: #fec40c;
    --yellow-pale: #fdf3d6;
    --gray: #808080;
    --gray-light: #b5b5b5;
    --ink: #1c1c1c;
    --navy: #0b1f4f;
    --navy-deep: #061233;
    --black: #000;
    --white: #fff;
  }
  * { margin: 0; padding: 0; box-sizing: border-box; }
  html, body { width: 808px; height: 1200px; overflow: hidden; background: var(--white); }
  body { position: relative; font-family: "Nunito", sans-serif; color: var(--ink); }
  .abs { position: absolute; }

  /* header */
  .site-header { position: absolute; left: 0; top: 0; width: 808px; height: 73px; background: var(--white); }
  .brand { position: absolute; left: 89px; top: 24px; font-weight: 700; font-size: 16px; color: #555; display: flex; align-items: center; gap: 6px; }
  .brand-square { width: 10px; height: 10px; background: var(--yellow); }
  .main-nav a { position: absolute; top: 29px; font-size: 9.6px; color: var(--ink); text-decoration: none; }

  /* hero */
  .hero { position: absolute; left: 0; top: 73px; width: 808px; height: 420px;
    background: radial-gradient(ellipse at 70% 40%, #12306e 0%, var(--navy) 45%, var(--navy-deep) 100%); overflow: hidden; }
  .hero-title { position: absolute; left: 83px; top: 55px; font-family: "Exo 2", sans-serif; font-weight: 600; font-size: 29px; line-height: 37px; color: var(--white); letter-spacing: 0.3px; }
  .hero-text { position: absolute; left: 85px; top: 218px; width: 252px; font-size: 10.4px; line-height: 17.3px; color: #e4e8f2; font-weight: 300; }
  .btn-primary { position: absolute; left: 87px; top: 325px; width: 102px; height: 35px; background: var(--yellow); color: var(--ink); font-weight: 800; font-size: 9.4px; display: flex; align-items: center; justify-content: center; text-decoration: none; }
  .globe { position: absolute; left: 395px; top: 42px; width: 337px; height: 337px; border-radius: 50%;
    background: radial-gradient(circle at 45% 45%, #5c7a3a 0%, #2d5fa0 28%, #1a4393 60%, #0e2a6c 100%); }

  /* slogan */
  .slogan { position: absolute; left: 0; top: 515px; width: 808px; height: 110px; }
  .slogan-plane { position: absolute; left: 191px; top: 4px; width: 30px; height: 14px; background: #8a8a8a; border-radius: 3px; }
  .slogan-top { position: absolute; left: 183px; top: 28px; width: 453px; height: 39px; background: var(--gray); color: var(--white);
    font-family: "Exo 2", sans-serif; font-weight: 600; font-size: 16px; display: flex; align-items: center; justify-content: center; }
  .slogan-bottom { position: absolute; left: 197px; top: 67px; width: 425px; height: 40px; background: var(--yellow); color: var(--white);
    font-family: "Exo 2", sans-serif; font-weight: 600; font-size: 16px; display: flex; align-items: center; justify-content: center; }

  /* facts */
  .facts { position: absolute; left: 86px; top: 674px; width: 632px; height: 167px; border: 1.2px solid var(--gray-light); }
  .facts-title { position: absolute; left: 280px; top: -10px; width: 72px; background: var(--white); text-align: center;
    font-family: "Exo 2", sans-serif; font-weight: 500; font-size: 15.5px; letter-spacing: 0.5px; }
  .fact { position: absolute; top: 29px; height: 118px; text-align: center; }
  .fact + .fact { border-left: 1px solid #e3e3e3; }
  .fact-icon { width: 30px; height: 30px; margin: 0 auto; border-radius: 50%; background: var(--yellow-pale); display: flex; align-items: center; justify-content: center; }
  .fact-value { margin-top: 9px; font-family: "Exo 2", sans-serif; font-weight: 500; font-size: 13px; }
  .fact-label { margin-top: 4px; font-size: 9.2px; line-height: 14px; color: #333; }

  /* tagline */
  .plane-art { position: absolute; left: 48px; top: 875px; width: 146px; height: 40px;
    background: linear-gradient(90deg, #f2f2f2, #d9d9d9); }
  .tagline { position: absolute; left: 184px; top: 907px; width: 539px; height: 43px; background: var(--yellow); z-index: 2;
    font-family: "Exo 2", sans-serif; font-weight: 500; font-size: 14.5px; color: var(--ink); display: flex; align-items: center; justify-content: center; }

  /* footer */
  .site-footer { position: absolute; left: 0; top: 934px; width: 808px; height: 266px; background: var(--black); color: var(--white); }
  .footer-brand { position: absolute; left: 89px; top: 96px; font-weight: 700; font-size: 27px; color: #6a6a6a; display: flex; align-items: center; gap: 10px; }
  .footer-brand .brand-square { width: 16px; height: 16px; }
  .footer-col { position: absolute; top: 56px; }
  .footer-col h4 { font-family: "Exo 2", sans-serif; font-weight: 600; font-size: 10px; margin-bottom: 7px; letter-spacing: 0.3px; }
  .footer-col a { display: block; font-size: 7.6px; line-height: 14px; color: var(--white); text-decoration: none; }
  .footer-rule { position: absolute; left: 88px; top: 199px; width: 630px; height: 1px; background: #333; }
  .copyright { position: absolute; left: 0; top: 227px; width: 808px; text-align: center; font-size: 7.6px; }
</style>
</head>
<body>

<header class="site-header">
  <div class="brand"><span>Brimleaf Tech</span><span class="brand-square"></span></div>
  <nav class="main-nav">
    <a style="left:264px" href="#">Industries</a>
    <a style="left:323px" href="#">Solutions</a>
    <a style="left:380px" href="#">Operational Support</a>
    <a style="left:488px" href="#">Case Studies</a>
    <a style="left:565px" href="#">Testimonials</a>
    <a style="left:636px" href="#">News</a>
    <a style="left:677px" href="#">About Us</a>
  </nav>
</header>

<section class="hero">
  <h1 class="hero-title">Seamlessly<br>connecting the air<br>cargo industry from<br>Manila to Tahiti</h1>
  <p class="hero-text">Blending decades of air cargo knowledge with end-to-end IT solutions. Whether you are an Airline, GSA, GHA, Forwarder or E-commerce Operator, our expertise can elevate your daily workflows, cutting down on expenses, time, and errors.</p>
  <a class="btn-primary" href="#">LEARN MORE</a>
  <div class="globe" role="img" aria-label="Globe showing Australia and the Pacific with a flight route from Manila to Tahiti"></div>
</section>

<section class="slogan">
  <svg class="abs" style="left:0;top:0" width="808" height="110" viewBox="0 0 808 110">
    <polyline points="183,55 112,55 112,69 192,69 192,105 124,105" fill="none" stroke="#b0b0b0" stroke-width="6"/>
    <polyline points="636,28 696,28 696,79 622,79" fill="none" stroke="#fec40c" stroke-width="6"/>
    <line x1="636" y1="65" x2="684" y2="65" stroke="#fec40c" stroke-width="6"/>
  </svg>
  <div class="slogan-plane" role="img" aria-label="Small gray airplane silhouette"></div>
  <div class="slogan-top">We are not IT tech experts attempting to do cargo!</div>
  <div class="slogan-bottom">We are cargo experts with programming skills!</div>
</section>

<section class="facts">
  <h2 class="facts-title">FACTS</h2>
  <div class="fact" style="left:0;width:85px">
    <div class="fact-icon"><svg width="18" height="18" viewBox="0 0 18 18" fill="none" stroke="#222" stroke-width="1.2"><path d="M2 10 l14 -5 M5 9 l-2 -3 M9 8 l2 -5 M2 15 h14"/></svg></div>
    <div class="fact-value">2014</div><div class="fact-label">Established</div>
  </div>
  <div class="fact" style="left:85px;width:78px">
    <div class="fact-icon"><svg width="18" height="18" viewBox="0 0 18 18" fill="none" stroke="#222" stroke-width="1.2"><circle cx="4" cy="7" r="2"/><circle cx="9" cy="5" r="2"/><circle cx="14" cy="7" r="2"/><path d="M1 13 q3 -4 6 0 M6 11 q3 -4 6 0 M11 13 q3 -4 6 0"/></svg></div>
    <div class="fact-value">22</div><div class="fact-label">Employees</div>
  </div>
  <div class="fact" style="left:163px;width:131px">
    <div class="fact-icon"><svg width="18" height="18" viewBox="0 0 18 18" fill="none" stroke="#222" stroke-width="1.2"><path d="M3 8 v-2 h12 l-3 -3 M15 10 v2 h-12 l3 3"/></svg></div>
    <div class="fact-value">11,500,000 +</div><div class="fact-label">Nr. of Annual Electronic<br>Exchanges</div>
  </div>
  <div class="fact" style="left:294px;width:109px">
    <div class="fact-icon"><svg width="18" height="18" viewBox="0 0 18 18" fill="none" stroke="#222" stroke-width="1.2"><circle cx="9" cy="9" r="7"/><path d="M4 6 q3 1 4 4 M11 3 q2 4 5 5"/></svg></div>
    <div class="fact-value">18</div><div class="fact-label">Countries covered</div>
  </div>
  <div class="fact" style="left:403px;width:109px">
    <div class="fact-icon"><svg width="18" height="18" viewBox="0 0 18 18" fill="none" stroke="#222" stroke-width="1.2"><circle cx="9" cy="9" r="2"/><circle cx="4" cy="4" r="1.6"/><circle cx="14" cy="4" r="1.6"/><circle cx="4" cy="14" r="1.6"/><circle cx="14" cy="14" r="1.6"/><path d="M5 5 l3 3 M13 5 l-3 3 M5 13 l3 -3 M13 13 l-3 -3"/></svg></div>
    <div class="fact-value">20+</div><div class="fact-label">Connected Clients</div>
  </div>
  <div class="fact" style="left:512px;width:120px">
    <div class="fact-icon"><svg width="18" height="18" viewBox="0 0 18 18" fill="none" stroke="#222" stroke-width="1.2"><rect x="2" y="3" width="14" height="13" rx="1"/><path d="M2 6 h14 M5 9 h2 M8 9 h2 M11 9 h2 M5 12 h2 M8 12 h2"/></svg></div>
    <div class="fact-value">350,000 +</div><div class="fact-label">Nr. of Annual AWBs</div>
  </div>
</section>

<div class="plane-art" role="img" aria-label="White passenger jet in flight trailing a thin looping flight path"></div>
<div class="tagline">Affordable IT Solutions That Revolutionize Tomorrow’s Air Cargo Today</div>

<footer class="site-footer">
  <div class="footer-brand"><span>Brimleaf Tech</span><span class="brand-square"></span></div>
  <div class="footer-col" style="left:371px">
    <h4>MENU</h4>
    <a href="#">Industries</a><a href="#">Solutions</a><a href="#">Operational Support</a><a href="#">Case Studies</a><a href="#">Testimonials</a><a href="#">News</a><a href="#">About Us</a>
  </div>
  <div class="footer-col" style="left:496px">
    <h4>SOLUTIONS</h4>
    <a href="#">Aerovance Carrier</a><a href="#">Aerovance Handler</a><a href="#">Waybillo</a><a href="#">RoadLink Cargo</a><a href="#">HiveDesk</a>
  </div>
  <div class="footer-col" style="left:610px">
    <h4>ABOUT US</h4>
    <a href="#">About Brimleaf Tech Our story</a><a href="#">Our ethos</a><a href="#">Sustainability</a><a href="#">Contact</a>
  </div>
  <div class="footer-rule"></div>
  <p class="copyright">Copyright © 2024 All Rights Reserved</p>
</footer>

</body>
</html>
```